website re-design - the brickfern studio

The Brickfern Studio is an existing website that we built using a new zealand based online CMS tool which is quite flexible and accomodates custom designs. You can check it here: http://www.pagequilt.co.nz/.

We have a logo already and the content on the website is OK.
The website can be found at www.thebrickfernstudio.com.au

mainly the homepage, but if the design is easily adapted to the other pages then, we will commission the winner to update these pages also.
Updates

Hi there,  I am uploading an image to be used as the main image on the homepage design,  so all submissions have the same image.

Target Market(s)

property developers, architects, builders, home buyers

Industry/Entity Type

Shop

Requirements
Must have
• Must utilise the existing CMS or at least be compatible to upload
Nice to have
• a promotional banner that can be turned off and on and changed as required as we offer different promotions over time.

```html
<!DOCTYPE html>
<html lang="en">
<head>
<meta charset="utf-8">
<title>The Brickfern Studio – Architectural Scale Models</title>
<link rel="stylesheet" href="https://fonts.googleapis.com/css2?family=Anton&family=Arimo:wght@400;700&family=Open+Sans:ital,wght@0,300;0,400;1,300&display=swap">
<style>
:root{
  --dark:#2b2b2b;
  --darker:#1c1c1c;
  --panel:#e7e7e7;
  --orange:#f07800;
  --orange-light:#ff9a1e;
  --text:#333;
  --muted:#8a8a8a;
  --blue:#1b8ff0;
  --green:#4cbd0a;
}
*{box-sizing:border-box;margin:0;padding:0}
html,body{width:857px;height:1200px;overflow:hidden}
body{position:relative;background:var(--dark);font-family:"Arimo",Arial,sans-serif;color:var(--text)}
.abs{position:absolute}

/* content panel */
.content-panel{left:254px;top:0;width:603px;height:1134px;background:var(--panel);border-bottom-left-radius:22px}

/* header */
.brand-mark{left:283px;top:36px;width:46px;height:46px;background:var(--orange)}
.brand-name{left:345px;top:46px;font-family:"Open Sans",sans-serif;font-size:25px;color:#222;letter-spacing:.5px;white-space:nowrap}
.brand-sub{left:346px;top:76px;font-family:"Open Sans",sans-serif;font-size:12px;color:var(--orange);letter-spacing:1px;white-space:nowrap}

/* side tab + nav */
.side-tab{left:27px;top:118px;width:228px;height:34px;background:linear-gradient(#ff9a28,#e56e00);border-radius:6px 0 0 6px;box-shadow:0 3px 5px rgba(0,0,0,.5)}
.side-tab span{display:block;text-align:center;font-family:"Anton",sans-serif;font-size:18px;line-height:34px;color:#3a1800;letter-spacing:.3px}
.main-nav{left:254px;top:118px;width:577px;height:34px;background:linear-gradient(#4a4a4a,#262626);border-radius:0 6px 6px 0;display:flex;align-items:center;padding-left:8px;box-shadow:0 3px 5px rgba(0,0,0,.4)}
.main-nav a{color:#e6e6e6;text-decoration:none;font-size:10px;padding:5px 8px;margin-right:1px}
.main-nav a.current{background:#111;color:var(--orange);border-radius:2px}

/* sidebar */
.search{left:56px;top:168px;width:188px;height:23px;background:#1f1f1f;border:1px solid #3a3a3a;display:flex;align-items:center}
.search span{flex:1;color:#999;font-size:10px;padding-left:7px}
.search i{width:24px;height:23px;background:var(--orange);display:flex;align-items:center;justify-content:center}
.tagline{left:30px;top:217px;width:214px;text-align:right;font-family:"Open Sans",sans-serif;font-weight:300;font-size:21px;line-height:25.5px;color:#8c8c8c}
.tagline b{font-weight:300;color:#d8d8d8;display:block;margin-top:2px}
.rule{left:40px;width:204px;border-top:1px dotted #777;height:0}

/* promotion banner */
.promo{left:32px;top:407px;width:209px;height:251px;background:linear-gradient(#6a6a6a 0 40%,#000 40%);border-radius:8px}
.promo-card{position:absolute;left:9px;top:8px;width:191px;height:233px;background:linear-gradient(#1c1c1c 0 54%,#484848 54%);border-radius:7px}
.promo-pct{position:absolute;left:0;top:22px;width:209px;text-align:center;font-family:"Anton",sans-serif;font-size:84px;line-height:100px;color:var(--orange);background:linear-gradient(#ffb000,#e65c00);-webkit-background-clip:text;background-clip:text;-webkit-text-fill-color:transparent}
.promo-text{position:absolute;left:0;top:137px;width:209px;text-align:center;font-family:"Anton",sans-serif;color:#f2f2f2;font-size:16px;line-height:17px;letter-spacing:.5px}
.promo-date{position:absolute;left:0;top:182px;width:209px;text-align:center;font-family:"Anton",sans-serif;color:#fff;font-size:19px;letter-spacing:.6px}

.side-title{left:40px;width:204px;text-align:right;font-family:"Open Sans",sans-serif;font-weight:300;font-size:17px;color:var(--orange);letter-spacing:-.3px}
.field{left:56px;width:188px;height:22px;background:#1f1f1f;border:1px solid #3a3a3a;color:#aaa;font-size:10px;line-height:20px;padding-left:4px}
.btn-small{left:162px;width:80px;height:24px;background:linear-gradient(#30a6ff,#0c74d8);font-family:"Anton",sans-serif;font-size:11px;color:#0b2d55;text-align:center;line-height:24px;letter-spacing:.3px}
.quote{left:50px;top:926px;width:192px;text-align:right;font-family:"Open Sans",sans-serif;font-style:italic;font-weight:300;font-size:13px;line-height:16.5px;color:#c9c9c9}
.quote-by{left:40px;top:1011px;width:201px;text-align:right;font-family:"Open Sans",sans-serif;font-weight:300;font-size:12.5px;color:#888}

/* slider */
.slider{left:271px;top:170px;width:540px;height:302px;border:3px solid #bdbdbd;background:#bdbdbd;box-shadow:0 6px 8px -4px rgba(0,0,0,.4)}
.slider-image{position:absolute;inset:0;background:linear-gradient(160deg,#3d4a45 0%,#6f7a78 35%,#a9aeb0 60%,#5a645f 100%)}
.slider-caption{position:absolute;left:0;right:0;bottom:0;height:47px;background:rgba(0,0,0,.62);color:#f2f2f2;font-family:"Open Sans",sans-serif;font-weight:300;font-size:13.5px;line-height:17.5px;padding:7px 0 0 18px}
.arrow{position:absolute;top:13px;width:27px;height:27px;border-radius:50%;background:linear-gradient(#fff,#cfcfcf);display:flex;align-items:center;justify-content:center}

/* main copy */
.h2{font-family:"Open Sans",sans-serif;font-weight:400;font-size:19.5px;color:#333}
.intro{left:271px;top:529px;font-family:"Open Sans",sans-serif;font-size:13px;line-height:16px;color:#444}
.checklist{left:311px;top:584px;width:505px;list-style:none}
.checklist li{position:relative;padding-left:22px;color:var(--orange);font-size:9.6px;line-height:12px;margin-bottom:12px}
.checklist svg{position:absolute;left:0;top:0}

.step-num{width:38px;height:38px;border-radius:50%;background:linear-gradient(#f4f4f4,#bdbdbd);border:1px solid #aaa;font-family:"Arimo",sans-serif;font-weight:700;font-size:19px;color:#333;text-align:center;line-height:36px}
.step-text{font-family:"Open Sans",sans-serif;font-size:16.5px;line-height:21px;color:#444}
.body-copy{left:286px;width:532px;font-size:9.4px;line-height:12px;color:#444}

.cta{top:1011px;width:177px;height:52px;border-radius:2px;font-family:"Anton",sans-serif;font-size:26px;text-align:center;line-height:52px;letter-spacing:.5px;box-shadow:0 6px 6px -3px rgba(0,0,0,.45)}
.cta-order{left:335px;background:linear-gradient(#34aaff,#0a72db);color:#0b2f5a}
.cta-quote{left:598px;background:linear-gradient(#6fdc1a,#3aa806);color:#10330a}
.cta-or{left:543px;top:1024px;font-family:"Anton",sans-serif;font-size:20px;color:#444}

/* footer */
.social{left:255px;top:1152px;display:flex;gap:10px}
.social span{width:27px;height:27px;border-radius:4px;background:linear-gradient(#f0f0f0,#b5b5b5);border:1px solid #888}
.copyright{left:400px;top:1159px;width:431px;text-align:right;font-size:9.6px;color:#9a9a9a}
</style>
</head>
<body>

<div class="abs content-panel"></div>

<!-- header -->
<div class="abs brand-mark"></div>
<div class="abs brand-name">THE BRICKFERN STUDIO</div>
<div class="abs brand-sub">ARCHITECTURAL SCALE MODELS</div>

<div class="abs side-tab"><span>THE BRICKFERN STUDIO</span></div>
<nav class="abs main-nav">
  <a class="current">Home</a><a>Gallery</a><a>Order Online</a><a>Get a Quote</a><a>Contact</a><a>3D Visualitation</a><a>About Us</a><a>Sitemap</a>
</nav>

<!-- sidebar -->
<div class="abs search"><span>search</span><i><svg width="14" height="14" viewBox="0 0 14 14"><circle cx="5.5" cy="5.5" r="4" fill="none" stroke="#fff" stroke-width="2"/><line x1="8.5" y1="8.5" x2="13" y2="13" stroke="#fff" stroke-width="2.4"/></svg></i></div>
<p class="abs tagline">A picture may be worth a thousand words, but<b>a model says it all</b></p>
<div class="abs rule" style="top:352px"></div>

<div class="abs promo">
  <div class="promo-card"></div>
  <div class="promo-pct">20%</div>
  <div class="promo-text">Off all models<br>ordered before</div>
  <div class="promo-date">31st December 2011</div>
</div>

<div class="abs rule" style="top:690px"></div>
<h3 class="abs side-title" style="top:712px">NEWSLETTER</h3>
<div class="abs field" style="top:740px">Your name</div>
<div class="abs field" style="top:775px">Email</div>
<div class="abs btn-small" style="top:810px">SUBSCRIBE</div>

<div class="abs rule" style="top:865px"></div>
<h3 class="abs side-title" style="top:888px">TESTIMONIALS</h3>
<p class="abs quote">“Nice work, great detail. Here...You can tailor your model to suit your project and budget needs”</p>
<p class="abs quote-by">- Jane Marlow -</p>
<div class="abs btn-small" style="top:1039px">READ MORE</div>

<!-- slider -->
<div class="abs slider">
  <div class="slider-image" role="img" aria-label="Scale model of a residential development with rows of houses and streets"></div>
  <div class="slider-caption">A scale model lets everyone involved, get a very clear<br>understanding of your building.
    <span class="arrow" style="left:444px"><svg width="10" height="12" viewBox="0 0 10 12"><path d="M8 0 L0 6 L8 12Z" fill="#aaa"/></svg></span>
    <span class="arrow" style="left:496px"><svg width="10" height="12" viewBox="0 0 10 12"><path d="M2 0 L10 6 L2 12Z" fill="#aaa"/></svg></span>
  </div>
</div>

<!-- what we do -->
<h2 class="abs h2" style="left:271px;top:497px">What we do?</h2>
<p class="abs intro">If you answered yes to any of the following questions,<br>then you should be using the brickfern studio.</p>
<ul class="abs checklist">
  <li><svg width="13" height="11" viewBox="0 0 13 11"><path d="M1 6 L5 10 L12 1" fill="none" stroke="#3aa20a" stroke-width="2.5"/></svg>Are you undertaking a new apartment development or land development and need a model for council approval or marketing purposes?</li>
  <li><svg width="13" height="11" viewBox="0 0 13 11"><path d="M1 6 L5 10 L12 1" fill="none" stroke="#3aa20a" stroke-width="2.5"/></svg>Are you getting a new house designed and built and need a clear understanding of how it will look?</li>
  <li><svg width="13" height="11" viewBox="0 0 13 11"><path d="M1 6 L5 10 L12 1" fill="none" stroke="#3aa20a" stroke-width="2.5"/></svg>Are you an architect or building designer looking for a more affordable way to add to your service?</li>
  <li><svg width="13" height="11" viewBox="0 0 13 11"><path d="M1 6 L5 10 L12 1" fill="none" stroke="#3aa20a" stroke-width="2.5"/></svg>Are you wanting to clarify in your own mind how your new building sits on its site?</li>
  <li><svg width="13" height="11" viewBox="0 0 13 11"><path d="M1 6 L5 10 L12 1" fill="none" stroke="#3aa20a" stroke-width="2.5"/></svg>Are you looking to for a way to market your buildings in an effective and affordable format that everyone can relate to?</li>
</ul>

<!-- steps -->
<h2 class="abs h2" style="left:275px;top:755px">It's this easy</h2>
<div class="abs step-num" style="left:287px;top:806px">1</div>
<p class="abs step-text" style="left:336px;top:803px;text-align:center">Order online or fill<br>in the quote form</p>
<svg class="abs" style="left:502px;top:806px" width="30" height="36" viewBox="0 0 30 36"><path d="M0 0 H12 L30 18 L12 36 H0 L18 18Z" fill="#4cbd0a"/></svg>
<div class="abs step-num" style="left:557px;top:806px">2</div>
<p class="abs step-text" style="left:602px;top:803px">We'll build your model and<br>deliver it right to your door</p>

<p class="abs body-copy" style="top:878px">You can tailor your model to suit your project and budget needs. There are various add-ons such as a display case, internal walls, acrylic windows, people trees and cars and site contours as well as a scaled pricing structure based on the size of your building.</p>
<p class="abs body-copy" style="top:927px">We have made the system very easy to use, so all you need to do is click your way to your new scale model. Just follow the prompts and away you go. Click here to order your model now. Or click here to get a quote.</p>

<div class="abs cta cta-order">ORDER NOW</div>
<div class="abs cta-or">OR</div>
<div class="abs cta cta-quote">GET A QUOTE</div>

<!-- footer -->
<div class="abs social"><span></span><span></span><span></span><span></span><span></span></div>
<p class="abs copyright">2011 © Copyright The Brickfern Studio - Site map Phone: (08) 5550 0147 Australia</p>

</body>
</html>
```